Business Card Design

We are starting up a new Family run Business mainly offering a Free House Clearance service. We also offer the following chargeable services which include a Removals Service, Delivery and Collection of Items sold or purchased on Bidloft, Swapcorner etc, including Motorcycles, Piano's, Furniture, Electrical appliances.
As there are a few Companies offering similar services we need to stand out and show what we do at a glance while appearing Professional and approachable
Updates

TidyNests

i  am liking some of the colours and designs so far but would like to see a few of our services listed as 1 or 2 have already done if this is possible and maybe some emphasis on the FREE House Clearance. thank you 
best regards
derek

Target Market(s)

Commercial and Domestic Tenants and Landlords aswell as Families looking for a friendly sympathetic clearance service after bereavement

Industry/Entity Type

Business

Contact Information for Business Card

TidyNests,
HouseClearance and Removals,
Brynmor Vale
CF47 2RL
Tel: 07831562904
Email: enquiries@tidynests.example

```html
<!DOCTYPE html>
<html lang="en">
<head>
<meta charset="utf-8">
<title>TidyNests Business Card</title>
<link rel="stylesheet" href="https://fonts.googleapis.com/css2?family=Lato:wght@400;700;900&display=swap">
<style>
  :root {
    --backdrop: #e6e7e9;
    --card: #ffffff;
    --ink: #2b2b2b;
    --accent: #27a4dd;
    --pattern-light: #f4fafd;
    --pattern-mid: #e3f2fa;
  }
  * { box-sizing: border-box; margin: 0; padding: 0; }
  html, body {
    width: 1200px;
    height: 926px;
    overflow: hidden;
    background: var(--backdrop);
    font-family: "Lato", sans-serif;
    color: var(--ink);
  }
  .sheet {
    position: relative;
    width: 1200px;
    height: 926px;
    display: flex;
    align-items: center;
    justify-content: center;
    gap: 60px;
  }
  .card {
    position: relative;
    width: 525px;
    height: 300px;
    background: var(--card);
    box-shadow: 0 6px 18px rgba(0,0,0,0.15);
    overflow: hidden;
  }
  /* Front */
  .brand-name {
    position: absolute;
    left: 42px;
    top: 34px;
    font-size: 30px;
    font-weight: 400;
    letter-spacing: 0.5px;
  }
  .accent-rule {
    position: absolute;
    left: 42px;
    width: 26px;
    height: 3px;
    background: var(--accent);
  }
  .accent-rule.contact-rule { top: 112px; }
  .accent-rule.service-rule { top: 198px; }
  .contact-list {
    position: absolute;
    left: 42px;
    top: 124px;
    list-style: none;
    font-size: 15px;
    font-weight: 700;
    line-height: 1.35;
  }
  .service-title {
    position: absolute;
    left: 42px;
    top: 210px;
    font-size: 21px;
    font-weight: 400;
  }
  .address {
    position: absolute;
    left: 42px;
    top: 240px;
    font-size: 15px;
    font-weight: 400;
  }
  /* Back */
  .pattern-field {
    position: absolute;
    inset: 0;
    background: linear-gradient(135deg, var(--pattern-light), var(--pattern-mid));
  }
  .offer-band {
    position: absolute;
    right: 0;
    top: 176px;
    width: 262px;
    height: 40px;
    background: var(--accent);
    color: #fff;
    font-size: 20px;
    font-weight: 400;
    display: flex;
    align-items: center;
    padding-left: 10px;
    white-space: nowrap;
  }
  .offer-band strong { font-weight: 900; margin-right: 5px; }
</style>
</head>
<body>
<main class="sheet">
  <section class="card card-front">
    <h1 class="brand-name">Tidy Nests</h1>
    <span class="accent-rule contact-rule"></span>
    <ul class="contact-list">
      <li>tel: 07831562904</li>
      <li>email: enquiries@tidynests.example</li>
    </ul>
    <span class="accent-rule service-rule"></span>
    <p class="service-title">House Clearance and Removals</p>
    <p class="address">Brynmor Vale CF47 2RL</p>
  </section>

  <section class="card card-back">
    <div class="pattern-field" role="img" aria-label="Light blue dot grid pattern on white"></div>
    <p class="offer-band"><strong>FREE</strong> House Clearance</p>
  </section>
</main>
</body>
</html>
```